Realtor business card

Looking for a business card that will stand out from the rest. My area of expertise is residential real estate and loans.

Industry/Entity Type

Residential

Requirements
Must have
• Owen Blakely, SFR
Broker
Mortgage Loan Originator
Notary Public
DRE License #07392518
NMLS 581637
Cell 714-529-4170
Fax 888-415-2967
www.owenblakely-example.com
ob@owenblakely-example.com

```html
<!DOCTYPE html>
<html lang="en">
<head>
<meta charset="utf-8">
<title>Owen Blakely, SFR – Business Card</title>
<link rel="stylesheet" href="https://fonts.googleapis.com/css2?family=Jost:ital,wght@0,300;0,400;0,700;1,300&family=Roboto+Condensed:wght@400&display=swap">
<style>
  :root {
    --stage: #434345;
    --ink: #1c1c1c;
    --ink-soft: #2a2a2a;
    --fine: #7a7a7a;
    --silver-dark: #8c8d90;
    --silver-mid: #b9babd;
    --silver-light: #eeeeef;
    --back-dark: #5b5b5d;
    --back-mid: #8e8e90;
    --back-light: #e4e4e4;
    --seal-face: #ffffff;
    --seal-rim: #9a9a9c;
  }
  html, body {
    margin: 0;
    width: 1200px;
    height: 927px;
    overflow: hidden;
    background: var(--stage);
  }
  .canvas {
    position: relative;
    width: 1200px;
    height: 927px;
  }
  .card {
    position: absolute;
    left: 218px;
    width: 763px;
    overflow: hidden;
  }
  .card-front {
    top: 12px;
    height: 436px;
    background: linear-gradient(115deg,
      var(--silver-dark) 0%, var(--silver-mid) 22%, var(--silver-light) 44%,
      var(--silver-mid) 58%, var(--silver-dark) 78%, var(--silver-mid) 100%);
    font-family: "Jost", sans-serif;
    color: var(--ink);
  }
  .brand-name {
    position: absolute;
    left: 28px;
    top: 78px;
    font-family: "Jost", sans-serif;
    font-weight: 700;
    font-size: 22px;
    color: var(--ink);
  }
  .licenses {
    position: absolute;
    right: 66px;
    top: 31px;
    width: 180px;
    text-align: center;
    font-size: 12px;
    font-weight: 300;
    line-height: 22px;
    color: var(--fine);
  }
  .name-arc {
    position: absolute;
    left: 0;
    top: 0;
  }
  .name-arc text {
    font-family: "Jost", sans-serif;
    font-weight: 700;
    font-size: 27px;
    fill: var(--ink);
  }
  .line {
    position: absolute;
    left: 0;
    width: 763px;
    text-align: center;
    white-space: nowrap;
  }
  .roles {
    top: 190px;
    font-family: "Roboto Condensed", sans-serif;
    font-size: 18px;
    color: var(--ink-soft);
  }
  .phones {
    top: 253px;
    font-size: 25px;
    font-weight: 400;
  }
  .sep { margin: 0 18px; }
  .roles .sep { margin: 0 14px; }
  .web {
    top: 328px;
    font-size: 26px;
    font-weight: 300;
    font-style: italic;
  }
  .email { top: 364px; }

  .card-back {
    top: 477px;
    height: 438px;
  }
  .back-pattern {
    position: absolute;
    inset: 0;
    background:
      radial-gradient(circle at 50% 50%, var(--back-light) 0%, var(--back-mid) 40%, var(--back-dark) 100%);
  }
  .seal {
    position: absolute;
    left: 232px;
    top: 69px;
    width: 300px;
    height: 300px;
    border-radius: 50%;
    background: var(--seal-face);
    box-shadow: inset 0 0 0 10px var(--seal-rim), 0 0 30px rgba(255,255,255,0.5);
  }
  .seal-name {
    position: absolute;
    left: 0;
    width: 763px;
    top: 196px;
    text-align: center;
    font-family: "Jost", sans-serif;
    font-weight: 700;
    font-size: 30px;
    line-height: 44px;
    color: var(--ink);
  }
</style>
</head>
<body>
<main class="canvas">
  <section class="card card-front" aria-label="Card front">
    <div class="brand-name">Owen Blakely</div>
    <div class="licenses">
      <div>DRE License #07392518</div>
      <div>NMLS 581637</div>
    </div>
    <svg class="name-arc" width="763" height="436" viewBox="0 0 763 436" aria-label="Owen Blakely, SFR">
      <defs>
        <path id="nameCurve" d="M 232 154 A 236 236 0 0 1 540 154"/>
      </defs>
      <text><textPath href="#nameCurve" startOffset="50%" text-anchor="middle">Owen Blakely, SFR</textPath></text>
    </svg>
    <div class="line roles">Broker<span class="sep">•</span>Mortgage Loan Originator<span class="sep">•</span>Notary Public</div>
    <div class="line phones">Cell: 714-529-4170<span class="sep">•</span>Fax: 888-415-2967</div>
    <div class="line web">www.owenblakely-example.com</div>
    <div class="line web email">ob@owenblakely-example.com</div>
  </section>

  <section class="card card-back" aria-label="Card back">
    <div class="back-pattern" role="img" aria-label="Repeating pattern of small monogram circles on a grey background with a soft central glow"></div>
    <div class="seal"></div>
    <div class="seal-name">Owen Blakely<br>Realty</div>
  </section>
</main>
</body>
</html>
```